We require a business card that promotes our Electrical business. Things we would like included are;
1) our business name, Bright Path Electrical and Communication
2) Our Electrical licence, EC 73620
3) Our ABN, 41 297 506 183
4) Our website, www.korvanelectric.com.au
5) Our Email, info@korvanelectric.com.au
6) Our contact number, 0462 158 704
7) Our address, 57 Larkfield Rd West Dunmore Perth 6109
8) Our logo, I will attach this (can you please change it so the ackground is white not black)
9) Our colours are red and white and perhaps some black
10) Managing Director Tomasz Relhuvan
11) the back to say 'notes' and have some lines for writing

Target Market(s)

General

Industry/Entity Type

Electrical

Contact Information for Business Card

Include the colour white, black and red.

Font styles to use
Sans Serif

Requirements
Nice to have
• A thunder bolt or a power point or a cord or something electrical, cartoon image of a cartoon like electrical tradie

```html
<!DOCTYPE html>
<html lang="en">
<head>
<meta charset="utf-8">
<title>Bright Path Electrical and Communication – Business Card</title>
<link rel="stylesheet" href="https://fonts.googleapis.com/css2?family=Source+Sans+3:wght@300;400;600;700&display=swap">
<style>
  :root {
    --stage: #3a3532;
    --card-black: #111111;
    --card-white: #ffffff;
    --brand-red: #e3262b;
    --text-light: #f2f2f2;
    --logo-grey: #d9d9d9;
    --rule: #1a1a1a;
  }
  * { margin: 0; padding: 0; box-sizing: border-box; }
  html, body {
    width: 1200px; height: 844px; overflow: hidden;
    background: var(--stage);
    font-family: "Source Sans 3", "Helvetica Neue", Arial, sans-serif;
  }
  .canvas {
    position: relative; width: 1200px; height: 844px;
  }
  .card {
    position: absolute; top: 268px;
    width: 540px; height: 309px;
    border-radius: 4px; overflow: hidden;
    box-shadow: 0 6px 18px rgba(0,0,0,.35);
  }
  .card--front { left: 40px; background: var(--card-black); }
  .card--back { left: 620px; background: var(--card-white); }

  .brand { color: var(--logo-grey); font-weight: 300; line-height: 1; }
  .brand__name { font-size: 52px; letter-spacing: .5px; display: flex; align-items: center; gap: 10px; }
  .brand__mark { width: 14px; height: 14px; border-radius: 50%; background: var(--brand-red); }
  .brand__tagline { font-size: 17px; letter-spacing: 1.6px; text-transform: uppercase; margin-top: 4px; }

  .card--front .brand { position: absolute; left: 34px; top: 48px; }

  .contact {
    position: absolute; right: 30px; top: 150px;
    text-align: right; color: var(--text-light);
    font-size: 14px; line-height: 21px;
  }
  .contact__legal { color: var(--brand-red); }
  .contact__legal span { color: var(--text-light); }
  .contact__row { display: flex; justify-content: flex-end; align-items: center; gap: 7px; }
  .contact__icon { width: 11px; height: 11px; flex: none; }
  .contact__row--plain { padding-right: 18px; }

  .person {
    position: absolute; left: 34px; bottom: 34px;
    color: var(--text-light); font-size: 15px; line-height: 20px;
  }
  .person__name { font-size: 19px; font-weight: 700; }
  .person__surname { color: var(--brand-red); }
  .person__role { margin-bottom: 18px; }

  .back__band {
    position: absolute; left: 0; top: 0; width: 100%; height: 108px;
    background: var(--card-black);
  }
  .card--back .brand { position: absolute; right: 34px; top: 22px; text-align: left; }
  .card--back .brand__name { font-size: 44px; }
  .card--back .brand__tagline { font-size: 14px; }
  .notes {
    position: absolute; left: 0; top: 118px; width: 100%;
    text-align: center; color: var(--brand-red);
    font-weight: 700; font-size: 22px;
  }
  .notes__line {
    position: absolute; left: 80px; right: 80px; height: 1px; background: var(--rule);
  }
  .notes__line--one { top: 200px; }
  .notes__line--two { top: 250px; }
</style>
</head>
<body>
<main class="canvas">

  <section class="card card--front" aria-label="Business card front">
    <div class="brand">
      <div class="brand__name">Bright Path <span class="brand__mark"></span></div>
      <div class="brand__tagline">Electrical and Communication</div>
    </div>

    <div class="contact">
      <div class="contact__legal">Electrical licence, EC <span>73620</span></div>
      <div class="contact__legal contact__row--plain">ABN, 41 297 506 183</div>
      <div class="contact__row">0462 158 704
        <svg class="contact__icon" viewBox="0 0 12 12" aria-hidden="true"><path d="M3 1l2 2.5-1.2 1.3a7 7 0 003.4 3.4L8.5 7 11 9l-1 2C5 11 1 7 1 2z" fill="var(--brand-red)"/></svg>
      </div>
      <div class="contact__row">info@korvanelectric.com.au
        <svg class="contact__icon" viewBox="0 0 12 12" aria-hidden="true"><rect x="0.5" y="2" width="11" height="8" fill="var(--brand-red)"/><path d="M0.5 2.5l5.5 4 5.5-4" stroke="var(--card-black)" fill="none"/></svg>
      </div>
      <div class="contact__row">www.korvanelectric.com.au
        <svg class="contact__icon" viewBox="0 0 12 12" aria-hidden="true"><circle cx="6" cy="6" r="5.5" fill="var(--brand-red)"/><path d="M1 6h10M6 0.5c-2.5 3-2.5 8 0 11M6 0.5c2.5 3 2.5 8 0 11" stroke="var(--card-black)" stroke-width=".8" fill="none"/></svg>
      </div>
    </div>

    <div class="person">
      <div class="person__name">Tomasz <span class="person__surname">Relhuvan</span></div>
      <div class="person__role">Managing Director</div>
      <address style="font-style:normal">Our address, 57 Larkfield Rd<br>West Dunmore Perth 6109</address>
    </div>
  </section>

  <section class="card card--back" aria-label="Business card back">
    <div class="back__band">
      <div class="brand">
        <div class="brand__name">Bright Path <span class="brand__mark"></span></div>
        <div class="brand__tagline">Electrical and Communication</div>
      </div>
    </div>
    <div class="notes">Notes</div>
    <div class="notes__line notes__line--one"></div>
    <div class="notes__line notes__line--two"></div>
  </section>

</main>
</body>
</html>
```